Overnight youth camp for refugee kids needs a brochure in Arabic

We need a 3-fold "Z" brochure for an overnight youth camp for Arabic speaking teens in Canada from the Middle East and Africa. The camp's name is Camp Falcon. Design should have an outdoors, sports theme and be attractive to teens and their parents. We will supply pictures and text in English. All but the Camp Falcon name should be in Arabic.

```html
<!DOCTYPE html>
<html lang="ar" dir="rtl">
<head>
<meta charset="utf-8">
<title>Camp Falcon – مطوية ثلاثية</title>
<link rel="stylesheet" href="https://fonts.googleapis.com/css2?family=Amiri:wght@400&family=Lalezar&display=swap">
<style>
  :root {
    --red: #8c2f1e;
    --green: #2c6332;
    --green-dark: #234f28;
    --green-band: #3a7a40;
    --paper: #f4f4f2;
    --ink-red: #9a2a1b;
    --ink-green: #2a5e2f;
    --ink-dark: #1f2a1f;
    --stage: #dcdcdc;
    --white: #ffffff;
  }
  * { box-sizing: border-box; margin: 0; padding: 0; }
  html, body { width: 1200px; height: 800px; overflow: hidden; background: var(--stage); }
  .brochure {
    position: absolute; left: 30px; top: 20px;
    width: 1140px; height: 760px;
    display: flex; flex-direction: row; direction: ltr;
    box-shadow: 0 6px 24px rgba(0,0,0,.18);
  }
  .panel { position: relative; width: 380px; height: 760px; overflow: hidden; background: var(--paper); direction: rtl; }
  .panel--middle { background: var(--green); }
  .panel-top { position: absolute; left: 0; top: 0; width: 380px; }
  .footer-bands { position: absolute; left: 0; bottom: 0; width: 100%; height: 45px; }
  .footer-bands .band-green { height: 25px; background: var(--green); }
  .footer-bands .band-red { height: 20px; background: var(--red); }

  .display { font-family: "Lalezar", "Arial Black", sans-serif; font-weight: 400; }
  .serif { font-family: "Amiri", "Times New Roman", serif; font-weight: 400; }

  /* Left panel */
  .program-heading { position: absolute; right: 28px; top: 74px; color: var(--ink-red); font-size: 26px; line-height: 34px; }
  .bullet-list { list-style: none; position: absolute; right: 30px; left: 20px; font-size: 18px; line-height: 23px; }
  .bullet-list li { position: relative; padding-right: 18px; }
  .bullet-list li::before {
    content: ""; position: absolute; right: 2px; top: 9px; width: 7px; height: 7px;
    background: currentColor; transform: rotate(45deg);
  }
  .program-list { top: 114px; color: var(--ink-red); }
  .cost-band {
    position: absolute; left: 0; top: 312px; width: 100%; height: 78px;
    background: var(--green-band); color: var(--white);
    font-size: 21px; line-height: 28px; padding: 11px 28px;
  }
  .fee-heading { position: absolute; right: 28px; top: 398px; color: var(--ink-green); font-size: 24px; line-height: 32px; }
  .fee-list { top: 438px; color: var(--ink-dark); }
  .photo-lake {
    position: absolute; left: 0; top: 590px; width: 100%; height: 125px;
    background: linear-gradient(180deg, #a9d0ee 0%, #cfe4f3 35%, #3f6f4a 52%, #4d7ea0 62%, #2f5d80 100%);
  }

  /* Middle panel */
  .intro { position: absolute; right: 30px; top: 78px; width: 320px; color: var(--white); }
  .intro-title { font-size: 24px; line-height: 30px; margin-bottom: 4px; direction: ltr; text-align: right; }
  .intro-text { font-size: 17px; line-height: 25px; }
  .values-box {
    position: absolute; left: 0; top: 256px; width: 100%; height: 172px;
    background: var(--green-dark); color: var(--white);
    font-size: 17px; line-height: 25px; padding: 22px 30px;
  }
  .contact { position: absolute; left: 0; top: 438px; width: 100%; text-align: center; color: var(--white); }
  .phone { font-size: 40px; line-height: 48px; letter-spacing: 1px; direction: ltr; }
  .address { font-size: 17px; line-height: 24px; margin-top: 4px; }
  .map-area {
    position: absolute; left: 0; top: 562px; width: 100%; height: 153px;
    background: linear-gradient(170deg, #e7eadf 0%, #d6e2c9 45%, #b9d7ea 70%, #a8cde6 100%);
  }

  /* Right panel */
  .cover-title {
    position: absolute; left: 40px; top: 40px; width: 300px; text-align: center;
    color: var(--white); font-size: 27px; line-height: 34px;
    transform: rotate(-14deg); transform-origin: center;
  }
  .photo-forest {
    position: absolute; left: 0; top: 180px; width: 100%; height: 300px;
    background: radial-gradient(ellipse at 55% 50%, #b9d99a 0%, #5f9a48 25%, #2f5a25 60%, #1b2e16 100%);
  }
  .cover-tagline {
    position: absolute; left: 30px; top: 396px; width: 320px; text-align: center;
    color: var(--white); font-size: 20px; line-height: 26px; transform: rotate(-10deg);
  }
  .cover-divider { position: absolute; left: 0; top: 470px; width: 380px; }
  .brand-block {
    position: absolute; left: 40px; top: 560px; width: 300px; height: 96px;
    background: var(--red); display: flex; direction: ltr; align-items: center; justify-content: center; gap: 14px;
  }
  .brand-mark { width: 22px; height: 22px; background: var(--paper); }
  .brand-name { color: var(--paper); font-size: 38px; line-height: 1; }
</style>
</head>
<body>
<main class="brochure">

  <section class="panel panel--left">
    <svg class="panel-top" width="380" height="80" viewBox="0 0 380 80">
      <path d="M0 0H380V8C250 14 120 40 0 66Z" fill="var(--red)"/>
      <path d="M0 66C120 40 250 14 380 8V24C250 30 120 52 0 72Z" fill="var(--green)"/>
    </svg>
    <h2 class="program-heading display">برنامجنا يشمل:</h2>
    <ul class="bullet-list program-list serif">
      <li>السباحة</li>
      <li>الألعاب الميدانية</li>
      <li>الحِرف اليدوية</li>
      <li>التزلّج بالعوّامات</li>
      <li>التجديف بالكانو</li>
      <li>جدار التسلّق</li>
      <li>سهرات حول نار المخيم</li>
      <li>مهارات البرية / مهارات الحياة في الطبيعة</li>
    </ul>
    <p class="cost-band display">التكلفة: يُطلب ٥٠ دولارًا مع طلب التسجيل لكل مخيِّم.</p>
    <h2 class="fee-heading display">رسومنا الشاملة تتضمّن:</h2>
    <ul class="bullet-list fee-list serif">
      <li>الوجبات والوجبات الخفيفة والألعاب الميدانية</li>
      <li>الطهي في الهواء الطلق والشواء</li>
      <li>استخدام الشاطئ والمعدات الرياضية</li>
      <li>مستلزمات الحِرف</li>
      <li>قرص DVD للمخيم</li>
      <li>صورة جماعية</li>
    </ul>
    <div class="photo-lake" role="img" aria-label="صورة مخيّمين يقفزون من رصيف خشبي إلى البحيرة"></div>
    <div class="footer-bands"><div class="band-green"></div><div class="band-red"></div></div>
  </section>

  <section class="panel panel--middle">
    <svg class="panel-top" width="380" height="80" viewBox="0 0 380 80">
      <path d="M0 0H380V42C250 30 120 22 0 24Z" fill="var(--red)"/>
      <path d="M0 24C120 22 250 30 380 42V54C250 42 120 38 0 40Z" fill="var(--green-dark)"/>
    </svg>
    <div class="intro">
      <h1 class="intro-title display">Camp Falcon</h1>
      <p class="intro-text serif">مخيم مبيت مصمَّم خصيصًا للفتيان والفتيات من الصومال وإثيوبيا وشمال أفريقيا والشرق الأوسط. نركّز على إعداد قادة الغد من خلال مغامرات تغيّر الحياة في خليقة الله.</p>
    </div>
    <p class="values-box serif">القيم المسيحية هي أساسنا، والمغامرة تملأ كل يوم! نحن ملتزمون بأن نقدّم لمخيّمينا تجربة العمر. تتكوّن الصداقات هنا وتستمر حتى بعد عودة المخيّمين إلى بيوتهم.</p>
    <div class="contact serif">
      <p class="phone">905.555.0142</p>
      <p class="address">بعناية: ١٤٧٠ ميبل ريدج درايف، الوحدة ١٢<br>برامبتون، أونتاريو L6X 2K4</p>
    </div>
    <div class="map-area" role="img" aria-label="خريطة طريق تُظهر مسار القيادة إلى المخيم على طول الساحل"></div>
    <div class="footer-bands"><div class="band-green"></div><div class="band-red"></div></div>
  </section>

  <section class="panel panel--right">
    <svg class="panel-top" width="380" height="182" viewBox="0 0 380 182">
      <path d="M0 0H380V70C250 100 120 140 0 170Z" fill="var(--red)"/>
      <path d="M0 170C120 140 250 100 380 70V82C250 112 120 152 0 182Z" fill="var(--green)"/>
    </svg>
    <h2 class="cover-title display">مغامرة صيفية<br>للفتيان والفتيات!</h2>
    <div class="photo-forest" role="img" aria-label="صورة ممر غابة مشمس تحت أشجار عالية"></div>
    <p class="cover-tagline display">قل سلام، سِلام، أو ببساطة مرحبًا<br>لصيف رائع!</p>
    <svg class="cover-divider" width="380" height="30" viewBox="0 0 380 30">
      <path d="M0 0H380V6C250 14 120 22 0 28Z" fill="var(--red)"/>
    </svg>
    <div class="brand-block">
      <span class="brand-mark"></span>
      <span class="brand-name display">Camp Falcon</span>
    </div>
    <div class="footer-bands"><div class="band-green"></div><div class="band-red"></div></div>
  </section>

</main>
</body>
</html>
```